Mobile Recording Studio needs business cards

Open to seeing a creative design, but I want to emphasis my logo and minimize the name/title and company information. Possible a fully black background on card.

My company is a mobile sound recording studio. ok to include a my trailer (actual or cartoon) on the card. My initial thought is more straight forward, but a good design will win me over.

SPECS:
CMYK color mode
High (300ppi) raster effect.
cover bleed area
please deliver: Illustrator file with layers and a pdf at completion.

Name and info for the business card:

Dallin Perry
ADR Mixer

email: Dallin@MixVault.com

address:
248 - 5170 East Hollister
Vancouver, BC V5R 2J4

phone:
604.518.2093 office

website:
www.MixVault.com

FB: @MixVault

Instagram: @TheMixVault

Industry/Entity Type

Television Production

Contact Information for Business Card

Dallin Perry
ADR Mixer

email: Dallin@MixVault.com

address:
248 - 5170 East Hollister
Vancouver, BC V5R 2J4

phone:
604.518.2093 office

website:
www.MixVault.com

FB: @MixVault

Instagram: @TheMixVault

Colors

Designer to choose colors to be used in the design.

Requirements
Must have
• emphasis my logo and minimize the name/title and company information.
• SPECS:
• CMYK color mode
• High (300ppi) raster effect.
• cover bleed area
• please deliver: Illustrator file with layers and a pdf at completion.
Nice to have
• maybe include the following:
• all black background or black theme
• my work trailer (actual or cartoon) refer to Instagram: @TheMixVault

```html
<!DOCTYPE html>
<html lang="en">
<head>
<meta charset="utf-8">
<title>MixVault Business Card</title>
<link href="https://fonts.googleapis.com/css2?family=Merriweather:wght@700;900&family=Roboto:wght@400;500&display=swap" rel="stylesheet">
<style>
  :root {
    --page-bg: #2f2f31;
    --card-black: #1b1b1c;
    --card-charcoal: #262627;
    --silver-light: #f4f4f4;
    --silver-mid: #cfcfd1;
    --silver-dark: #9a9a9c;
    --logo-silver: #d6d6d8;
    --ink: #111111;
    --ink-soft: #2a2a2a;
    --white: #ffffff;
  }
  * { margin: 0; padding: 0; box-sizing: border-box; }
  html, body { width: 799px; height: 1200px; overflow: hidden; background: var(--page-bg); }
  .canvas { position: relative; width: 799px; height: 1200px; }
  .card {
    position: absolute; left: 80px; width: 640px; height: 366px;
    overflow: hidden; box-shadow: 0 18px 40px rgba(0,0,0,0.45);
  }
  .card--front { top: 130px; background: var(--card-black); }
  .card--back { top: 700px; background: var(--card-charcoal); }
  .card-shapes { position: absolute; inset: 0; }
  .logo-word {
    font-family: "Merriweather", Georgia, serif; font-weight: 900;
    color: var(--logo-silver); letter-spacing: 1px; white-space: nowrap;
  }
  .card--front .logo-word {
    position: absolute; left: 0; right: 0; top: 140px;
    text-align: center; font-size: 64px;
  }
  .card--back .logo-word {
    position: absolute; left: 330px; width: 300px; top: 130px;
    text-align: center; font-size: 50px;
  }
  .holder { position: absolute; left: 42px; top: 44px; }
  .holder-name {
    font-family: "Merriweather", Georgia, serif; font-weight: 900;
    font-size: 22px; color: var(--ink);
  }
  .holder-title {
    font-family: "Roboto", Arial, sans-serif; font-size: 12px;
    color: var(--ink-soft); margin-top: 3px;
  }
  .contact {
    position: absolute; left: 42px; top: 196px;
    font-family: "Roboto", Arial, sans-serif; font-size: 15px;
    color: var(--ink); line-height: 22px;
  }
  .contact-row { display: flex; align-items: center; gap: 10px; }
  .contact-row svg { width: 13px; height: 13px; flex: none; }
  .contact-address { padding-left: 23px; }
  .socials {
    position: absolute; left: 360px; top: 228px; width: 260px;
    display: flex; justify-content: center; gap: 18px;
    font-family: "Roboto", Arial, sans-serif; font-size: 15px; color: var(--white);
  }
  .social { display: flex; align-items: center; gap: 7px; }
  .social-dot { width: 12px; height: 12px; border-radius: 50%; background: var(--silver-mid); }
</style>
</head>
<body>
<main class="canvas">

  <section class="card card--front" aria-label="Card front">
    <div class="logo-word">MixVault</div>
  </section>

  <section class="card card--back" aria-label="Card back">
    <svg class="card-shapes" viewBox="0 0 640 366" width="640" height="366" aria-hidden="true">
      <defs>
        <linearGradient id="silverPanel" x1="0" y1="0" x2="1" y2="1">
          <stop offset="0" stop-color="#d9d9db"/>
          <stop offset="0.45" stop-color="#f6f6f6"/>
          <stop offset="0.7" stop-color="#c9c9cb"/>
          <stop offset="1" stop-color="#e4e4e5"/>
        </linearGradient>
      </defs>
      <rect class="silver-panel" width="640" height="366" fill="url(#silverPanel)"/>
      <path class="curve-band" d="M388 0 C318 80 292 200 290 366 L640 366 L640 0 Z" fill="#8e8e90"/>
      <path class="dark-panel" d="M400 0 C332 80 306 200 304 366 L640 366 L640 0 Z" fill="#262627"/>
    </svg>

    <div class="holder">
      <div class="holder-name">Dallin Perry</div>
      <div class="holder-title">ADR Mixer</div>
    </div>

    <div class="contact">
      <div class="contact-address">248 - 5170 East Hollister</div>
      <div class="contact-address">Vancouver, BC V5R 2J4</div>
      <div class="contact-row">
        <svg viewBox="0 0 16 16"><path d="M3 2h3l1 4-2 1c1 2 2 3 4 4l1-2 4 1v3c0 1-1 2-2 2C7 15 1 9 1 4c0-1 1-2 2-2z" fill="#1a1a1a"/></svg>
        <span>604.518.2093</span>
      </div>
      <div class="contact-row">
        <svg viewBox="0 0 16 16"><rect x="1" y="3" width="14" height="10" fill="#1a1a1a"/><path d="M1 3l7 6 7-6" stroke="#eee" stroke-width="1.2" fill="none"/></svg>
        <span>Dallin@MixVault.com</span>
      </div>
      <div class="contact-row">
        <svg viewBox="0 0 16 16"><circle cx="8" cy="8" r="6.5" fill="none" stroke="#1a1a1a" stroke-width="1.5"/><ellipse cx="8" cy="8" rx="2.8" ry="6.5" fill="none" stroke="#1a1a1a" stroke-width="1.2"/><path d="M1.5 8h13" stroke="#1a1a1a" stroke-width="1.2"/></svg>
        <span>www.MixVault.com</span>
      </div>
    </div>

    <div class="logo-word">MixVault</div>

    <div class="socials">
      <div class="social"><span class="social-dot"></span><span>@MixVault</span></div>
      <div class="social"><span class="social-dot"></span><span>@TheMixVault</span></div>
    </div>
  </section>

</main>
</body>
</html>
```